IT Consulting Site Revamping for Marlune

I've put a skeleton together on my website, but realize I need some help (it's http://pilot.marlune-example.ca).
I've pulled together tidbits from other websites, but really need my site to be cleaned up, and really spruced up.
I primarily focus on the IT needs of small to medium size businesses, taking care of everything from their servers and networks down to their workstations.
I also want a page listing the vendors (and logos) that I work with including Quillsoft, Zentrix, Halvor, Brax, TL, RZO, VELK, Trevo, Gatemoor.
There should also be a simple form to get a quote that will email me.
The final design should communicate strength and reliability.
I would like this to be a fully functional website, that I can upload to Plumly Pages, with the same sort of pages that are existing on http://pilot.marlune-example.ca
Updates
Hey everyone,
Hi everyone,
Reason: Hi all,
There are some designers that would like to submit some new designs, so I'm extending the deadline.
Thanks,
Target Market(s)
Small to medium size business owners. This will primarily be males who work in the oil and gas industry.
Industry/Entity Type
Consulting
Look and feel
Each slider illustrates characteristics of the customer's brand and the style your logo design should communicate.

```html
<!DOCTYPE html>
<html lang="en">
<head>
<meta charset="utf-8">
<title>Marlune Solutions</title>
<link rel="stylesheet" href="https://fonts.googleapis.com/css2?family=Open+Sans:wght@400;600;700&family=Oswald:wght@500;600&family=Roboto+Condensed:wght@400;700&display=swap">
<style>
:root{
  --blue:#0a7fc7;
  --blue-dark:#0569ad;
  --sky:#04b4f4;
  --ink:#333;
  --grey:#666;
  --light:#f4f4f4;
  --white:#fff;
}
*{box-sizing:border-box;margin:0;padding:0}
html,body{width:1177px;height:1200px;overflow:hidden;background:var(--light)}
body{font-family:"Open Sans",Arial,sans-serif;color:var(--ink);position:relative}
.page{position:relative;width:1177px;height:1200px;overflow:hidden;background:linear-gradient(#fafafa,#f1f1f1)}
.abs{position:absolute}

/* header */
.site-header{position:absolute;left:0;top:0;width:1177px;height:120px;background:#f9f9f9}
.brand{left:48px;top:18px;display:flex;align-items:center;gap:14px}
.brand-mark{width:92px;height:92px;border-radius:50%;background:var(--blue)}
.brand-name{font-family:"Open Sans",sans-serif;font-weight:700;font-size:48px;color:var(--blue);line-height:1;letter-spacing:-1px}
.brand-tag{font-size:14px;letter-spacing:8px;color:var(--grey);margin-top:4px}
.phone{right:48px;top:12px;display:flex;align-items:center;gap:8px;font-family:"Roboto Condensed",sans-serif;font-weight:700;font-size:25px;color:var(--blue)}
.main-nav{top:82px;left:0;width:1177px;font-family:"Roboto Condensed",sans-serif;font-size:18px;color:#333}
.main-nav a{position:absolute;color:inherit;text-decoration:none}
.main-nav a.active{color:var(--blue)}

/* hero */
.hero{left:0;top:119px;width:1177px;height:380px}
.hero-title{left:67px;top:156px;font-family:"Oswald",sans-serif;font-weight:600;font-size:44px;color:var(--white);letter-spacing:.5px;text-transform:uppercase;text-shadow:0 2px 3px rgba(0,0,0,.2)}
.hero-text{left:70px;top:253px;width:560px;font-size:14px;font-weight:600;line-height:20px;color:var(--white)}
.btn-more{left:446px;top:358px;width:172px;height:42px;border-radius:21px;background:#fff;border:5px solid #0a5f94;display:flex;align-items:center;justify-content:center;gap:10px;font-family:"Roboto Condensed",sans-serif;font-weight:700;font-size:17px;color:#333}
.btn-more i{width:22px;height:22px;border-radius:50%;background:#222;display:inline-flex;align-items:center;justify-content:center}
.hero-art{left:770px;top:146px;width:346px;height:298px;border-radius:12px;background:radial-gradient(circle at 50% 55%,rgba(255,255,255,.35),rgba(255,255,255,0) 70%)}
.slider-dots{left:537px;top:466px;display:flex;gap:9px}
.slider-dots span{width:13px;height:13px;border-radius:50%;background:var(--sky);border:2px solid #0d7fc0}
.slider-dots span.on{background:#c28a0d;border-color:#8d6307}

/* services */
.service{top:524px;width:172px;text-align:center}
.service svg{display:block;margin:0 auto}
.service-art{position:absolute;left:40px;top:25px;width:92px;height:92px;border-radius:50%;background:radial-gradient(circle,#c9d4dc,#eef2f5)}
.service h3{font-family:"Roboto Condensed",sans-serif;font-weight:400;font-size:18px;color:#333;margin-top:22px;white-space:nowrap;margin-left:-20px;margin-right:-20px}
.arrow{top:555px;width:40px;height:110px}

/* quote */
.quote{left:70px;top:826px;width:1040px;height:104px;background:#fff}
.quote p{position:absolute;left:40px;top:34px;width:960px;text-align:center;font-size:13.5px;line-height:20px;color:#555}
.quote .mark{position:absolute;font-family:Georgia,serif;font-size:70px;color:#999;line-height:1}

/* footer panels */
.footer-panels{left:0;top:932px;width:1177px;height:208px;border-top:2px solid #ddd}
.panel{position:absolute;top:0;height:208px}
.panel-follow{left:0;width:359px;background:#f3f3f3}
.panel-subscribe{left:359px;width:392px;background:linear-gradient(90deg,#e6e6e6,#f7f7f7 50%,#e6e6e6)}
.panel-connect{left:751px;width:426px;background:#f6f6f6}
.panel h2{position:absolute;font-weight:400;font-size:26px;color:var(--blue)}
.rule{position:absolute;height:1px;background:linear-gradient(90deg,transparent,#ccc,transparent)}
.social{position:absolute;left:96px;top:76px;display:flex;gap:14px;font-size:12px;font-weight:600;color:#555}
.social span{display:flex;flex-direction:column;align-items:center;gap:4px}
.social b{width:26px;height:26px;border-radius:50%;background:#555;display:block}
.social b.sky{background:#25b6e6}
.lorem{position:absolute;left:93px;top:138px;font-size:13px;font-weight:700;color:#888;line-height:22px}
.envelopes{left:226px;top:18px;width:150px;height:110px;border-radius:8px;background:linear-gradient(150deg,#fafafa,#c9c9c9)}
.subscribe-box{left:36px;top:88px;width:324px;height:92px;border-radius:10px;background:linear-gradient(#8a8a8a,#5c5c5c);border:3px solid #d8d8d8}
.subscribe-box h4{position:absolute;left:12px;top:8px;font-family:"Roboto Condensed",sans-serif;font-weight:700;font-size:21px;color:#fff}
.subscribe-box .field{position:absolute;left:15px;top:42px;width:176px;height:34px;background:#fff;border:3px solid #bbb;font-size:15px;color:#555;padding:4px 6px}
.subscribe-box .submit{position:absolute;left:198px;top:40px;width:78px;height:38px;background:linear-gradient(#2fa4ea,#0a6cc0);border:2px solid #1a4f83;color:#fff;font-family:"Roboto Condensed",sans-serif;font-weight:700;font-size:18px;text-align:center;line-height:34px}
.fb-row{position:absolute;left:22px;top:66px;display:flex;align-items:center;gap:8px;font-size:11px;color:#222;line-height:14px}
.fb-name{font-weight:700;color:#3b5998;font-size:12px}
.like-btn{border:1px solid #9aa9c8;background:#eceef5;padding:2px 6px;font-size:11px;color:#3b5998;border-radius:2px}
.tw-row{position:absolute;left:22px;top:128px;display:flex;align-items:center;gap:8px;font-size:13px}
.tw-name{font-weight:700;color:#25b6e6;font-size:12px;margin-right:6px}
.tw-box{border:1px solid #bbb;background:linear-gradient(#fff,#e6e6e6);padding:3px 10px;color:#333}

/* bottom bar */
.bottom-bar{left:0;top:1140px;width:1177px;height:60px;background:#f0f0f0}
.bottom-nav{position:absolute;left:93px;top:23px;font-size:12px;font-weight:600;color:#444}
.bottom-nav em{font-style:normal;color:#aaa;margin:0 5px}
.copyright{position:absolute;right:100px;top:23px;font-size:12px;font-weight:600;color:#555}
</style>
</head>
<body>
<div class="page">

  <header class="site-header">
    <div class="brand abs">
      <div class="brand-mark"></div>
      <div>
        <div class="brand-name">Marlune</div>
        <div class="brand-tag">solutions</div>
      </div>
    </div>
    <div class="phone abs">
      <svg width="24" height="20" viewBox="0 0 24 20" aria-hidden="true"><path d="M2 7c0-4 20-4 20 0v2h-5V6H7v3H2z" fill="#0a7fc7"/><rect x="5" y="11" width="14" height="8" rx="2" fill="#0a7fc7"/></svg>
      555-014-2280
    </div>
    <nav class="main-nav abs">
      <a class="active" style="left:573px">Home</a>
      <a style="left:656px">About Us</a>
      <a style="left:762px">Our Services</a>
      <a style="left:893px">Our Products</a>
      <a style="left:1027px">Contact Us</a>
    </nav>
  </header>

  <svg class="hero abs" viewBox="0 0 1177 380" aria-hidden="true">
    <defs>
      <linearGradient id="heroFill" x1="0" y1="0" x2="0" y2="1">
        <stop offset="0" stop-color="#06b8f6"/>
        <stop offset="1" stop-color="#0566b5"/>
      </linearGradient>
    </defs>
    <path d="M0 0H1177V366Q588 286 0 366Z" fill="url(#heroFill)"/>
    <path d="M582 0l10 -10 10 10z" fill="#06b8f6"/>
  </svg>
  <h1 class="hero-title abs">Easy, Affordable and Reliable IT Services</h1>
  <p class="hero-text abs">We have a diversity of small business support solutions. We provide in office, over the phone, remote or drop-off computer technical support services to small business.</p>
  <div class="btn-more abs">More Details <i><svg width="10" height="10" viewBox="0 0 10 10"><path d="M2 1l7 4-7 4z" fill="#fff"/></svg></i></div>
  <div class="hero-art abs" role="img" aria-label="Illustration of colourful figures on a connected network"></div>
  <div class="slider-dots abs"><span class="on"></span><span></span><span></span><span></span><span></span></div>

  <svg class="arrow abs" style="left:40px" viewBox="0 0 40 110" aria-hidden="true"><path d="M40 0Q0 55 40 110Z" fill="#ececec"/><path d="M24 40l-12 15 12 15" stroke="#999" stroke-width="4" fill="none"/></svg>
  <svg class="arrow abs" style="left:1097px" viewBox="0 0 40 110" aria-hidden="true"><path d="M0 0Q40 55 0 110Z" fill="#ececec"/><path d="M14 40l12 15-12 15" stroke="#999" stroke-width="4" fill="none"/></svg>

  <div class="service abs" style="left:96px">
    <svg width="172" height="222" viewBox="0 0 172 222" aria-hidden="true"><defs><linearGradient id="pin" x1="0" y1="0" x2="0" y2="1"><stop offset="0" stop-color="#0c8fdb"/><stop offset="1" stop-color="#3fc4f8"/></linearGradient></defs><path d="M86 4C40 4 4 40 4 84c0 45 40 78 82 134 42-56 82-89 82-134C168 40 132 4 86 4z" fill="url(#pin)"/><circle cx="86" cy="84" r="70" fill="#fff"/></svg>
    <div class="service-art" role="img" aria-label="Icon of silver gears"></div>
    <h3>Managed IT Services</h3>
  </div>
  <div class="service abs" style="left:298px">
    <svg width="172" height="222" viewBox="0 0 172 222" aria-hidden="true"><path d="M86 4C40 4 4 40 4 84c0 45 40 78 82 134 42-56 82-89 82-134C168 40 132 4 86 4z" fill="url(#pin)"/><circle cx="86" cy="84" r="70" fill="#fff"/></svg>
    <div class="service-art" role="img" aria-label="Icon of a stacked storage drum"></div>
    <h3>Storage and Virtualization</h3>
  </div>
  <div class="service abs" style="left:500px">
    <svg width="172" height="222" viewBox="0 0 172 222" aria-hidden="true"><path d="M86 4C40 4 4 40 4 84c0 45 40 78 82 134 42-56 82-89 82-134C168 40 132 4 86 4z" fill="url(#pin)"/><circle cx="86" cy="84" r="70" fill="#fff"/></svg>
    <div class="service-art" role="img" aria-label="Icon of a blue globe"></div>
    <h3>Networking</h3>
  </div>
  <div class="service abs" style="left:702px">
    <svg width="172" height="222" viewBox="0 0 172 222" aria-hidden="true"><path d="M86 4C40 4 4 40 4 84c0 45 40 78 82 134 42-56 82-89 82-134C168 40 132 4 86 4z" fill="url(#pin)"/><circle cx="86" cy="84" r="70" fill="#fff"/></svg>
    <div class="service-art" role="img" aria-label="Icon of discs and a hard drive"></div>
    <h3>Backup and Recovery</h3>
  </div>
  <div class="service abs" style="left:904px">
    <svg width="172" height="222" viewBox="0 0 172 222" aria-hidden="true"><path d="M86 4C40 4 4 40 4 84c0 45 40 78 82 134 42-56 82-89 82-134C168 40 132 4 86 4z" fill="url(#pin)"/><circle cx="86" cy="84" r="70" fill="#fff"/></svg>
    <div class="service-art" role="img" aria-label="Icon of a desktop monitor with a gear"></div>
    <h3>Computer Repair Service</h3>
  </div>

  <section class="quote abs">
    <span class="mark" style="left:2px;top:14px">&ldquo;</span>
    <p>Marlune has been trusted for over the last 7 years by small business companies like yours. Whether you are looking for an ongoing computer support company, looking to outsource your small business computer work, or just looking for a computer company to help you solve a computer problem,</p>
    <span class="mark" style="right:0;top:44px">&rdquo;</span>
  </section>

  <section class="footer-panels abs">
    <div class="panel panel-follow">
      <h2 style="left:95px;top:10px">Follow us on:</h2>
      <div class="rule" style="left:66px;top:52px;width:274px"></div>
      <div class="social">
        <span><b class="sky"></b>Chirply</span>
        <span><b></b>Vidora</span>
        <span><b></b>Circlo</span>
        <span><b></b>Facelink</span>
        <span><svg width="26" height="26" viewBox="0 0 26 26" aria-label="Email"><circle cx="13" cy="13" r="13" fill="#555"/><rect x="7" y="9" width="12" height="8" fill="#fff"/><path d="M7 9l6 5 6-5" stroke="#555" fill="none"/></svg>Mail</span>
      </div>
      <p class="lorem">Lorem ipsum dolor sit amet, cose<br>&nbsp;adipiscing elit.</p>
    </div>

    <div class="panel panel-subscribe">
      <div class="envelopes abs" role="img" aria-label="Illustration of flying envelopes"></div>
      <div class="subscribe-box abs">
        <h4>Subscribe to startup</h4>
        <div class="field">email@domain.com</div>
        <div class="submit">Submit</div>
      </div>
    </div>

    <div class="panel panel-connect">
      <h2 style="left:54px;top:10px">Connect with us</h2>
      <div class="rule" style="left:30px;top:52px;width:330px"></div>
      <div class="fb-row">
        <span class="fb-name">Facelink</span>
        <span class="like-btn">Like</span>
        <span>4 PEOPLE LIKE THIS. BE THE FIRST<br>OF YOUR FRIENDS.</span>
      </div>
      <div class="tw-row">
        <span class="tw-name">Chirply</span>
        <span class="tw-box">Follow@marlune</span>
        <span class="tw-box">559 followers</span>
      </div>
    </div>
  </section>

  <footer class="bottom-bar abs">
    <nav class="bottom-nav">Home<em>/</em>About Us<em>/</em>Our Services<em>/</em>Our Products<em>/</em>Contact Us</nav>
    <p class="copyright">Copyright ©2012-2013 All Rights Reserved</p>
  </footer>

</div>
</body>
</html>
```